I need a better looking dashboard for my web application

I have a very table heavy web page that I would like to add a design touch to it. I have the logo and primary colors picked out, I just need some help in adding visual appeal the page. I would also like to add a couple of button to the page as shortcuts. Every spot that has a + sign could have a button added. I would also like to add another graph (the data will be in the uploaded files. Please feel free to ask any questions :-)

```html
<!DOCTYPE html>
<html lang="en">
<head>
<meta charset="utf-8">
<title>ShiftCover Dashboard</title>
<link href="https://fonts.googleapis.com/css2?family=Open+Sans:wght@400;500;600;700&display=swap" rel="stylesheet">
<style>
:root{
  --backdrop:#777777;
  --purple:#6b51a5;
  --purple-mid:#9a78dc;
  --purple-light:#cbb8f0;
  --teal:#29b0d3;
  --teal-soft:#e3f5f9;
  --teal-line:#9fd9e9;
  --ink:#2e2e38;
  --muted:#8a8a96;
  --line:#e7e7ee;
  --page:#f9f9fd;
  --green:#1e9e5a;
  --red:#e0303a;
}
*{box-sizing:border-box;margin:0;padding:0}
html,body{width:1200px;height:1200px;overflow:hidden;background:var(--backdrop);font-family:"Open Sans",sans-serif;color:var(--ink)}
.stage{position:absolute;left:0;top:0;width:1932px;height:1932px;transform:scale(.62112);transform-origin:0 0}
.screen{position:absolute;left:341px;width:1287px;height:836px;background:var(--page);overflow:hidden}
.screen.first{top:104px}.screen.second{top:992px}
.sidebar{position:absolute;left:0;top:0;width:235px;height:100%;background:var(--purple);color:#fff}
.brand{position:absolute;left:42px;top:34px;display:flex;align-items:center;gap:8px;font-size:24px;font-weight:600}
.brand-dot{width:26px;height:26px;border-radius:50%;background:#fff}
.nav-item{position:absolute;left:22px;width:194px;height:34px;display:flex;align-items:center;font-size:14px;padding-left:16px;gap:14px;border-radius:2px}
.nav-item svg{width:17px;height:17px;fill:none;stroke:#fff;stroke-width:1.6}
.nav-item.sub{padding-left:31px}
.nav-item.active{background:var(--teal);font-weight:600}
.nav-item .caret{position:absolute;right:14px}
.avatar-main{position:absolute;left:272px;top:33px;width:60px;height:60px;border-radius:50%;border:3px solid var(--teal);background:radial-gradient(circle at 50% 40%,#d8b79c,#6fb9d3)}
.welcome{position:absolute;left:356px;top:24px;font-size:15px}
.user-name{position:absolute;left:355px;top:40px;font-size:32px;font-weight:700;color:var(--purple);display:flex;align-items:center;gap:22px}
.user-name svg{width:14px;height:14px;stroke:var(--teal);fill:none;stroke-width:2}
.top-btn{position:absolute;top:45px;height:34px;border:1.5px solid #dedee6;background:#fff;font-size:14px;display:flex;align-items:center;justify-content:center;color:#555;border-radius:2px}
.top-btn.soft{background:var(--teal-soft);border-color:var(--teal-line);color:var(--ink)}
.card{position:absolute;top:116px;width:304px;height:140px;background:#fff;border:1px solid var(--line);border-radius:6px}
.card-title{position:absolute;left:31px;top:18px;font-size:15px;font-weight:600}
.big-num{position:absolute;left:29px;top:38px;font-size:34px;font-weight:400;line-height:44px}
.meter{position:absolute;left:111px;top:59px;width:173px;height:4px;background:var(--purple);border-radius:2px;overflow:hidden}
.meter i{display:block;height:100%;width:22%;background:var(--purple-light)}
.meter.thick{top:56px;height:10px;border-radius:3px}
.legend{position:absolute;top:88px;font-size:14px}
.legend b{font-weight:400;display:flex;align-items:center;gap:8px}
.legend b::before{content:"";width:8px;height:8px;border-radius:50%;background:var(--dot)}
.legend span{display:block;color:var(--muted);font-size:13px;margin-top:2px}
.l1{--dot:var(--purple-light)}.l2{--dot:var(--purple-mid)}.l3{--dot:var(--purple)}
.cbar{position:absolute;display:flex;align-items:center;justify-content:center;font-size:14px}
.cbar-label{position:absolute;top:111px;width:64px;text-align:center;font-size:13px;color:var(--muted);margin-left:-6px}
.axis{position:absolute;font-size:9px;color:var(--muted);text-align:right;width:32px}
.stack{position:absolute;left:75px;width:82px;font-size:9px;color:#fff;display:flex;align-items:center;justify-content:center}
.side-legend{position:absolute;left:210px;font-size:13px;color:var(--muted);display:flex;align-items:center;gap:8px}
.side-legend::before{content:"";width:8px;height:8px;border-radius:50%;background:var(--dot)}
.tabs{position:absolute;left:296px;top:302px;display:flex;gap:24px;font-size:15px;color:#666}
.tabs .on{color:var(--teal);position:relative}
.tabs .on::after{content:"";position:absolute;left:0;right:0;top:35px;height:3px;background:var(--teal)}
.panel{position:absolute;left:277px;top:344px;width:971px;height:453px;background:#fff;border:1px solid var(--line);border-radius:6px}
.panel-title{position:absolute;left:30px;top:22px;font-size:20px;font-weight:500}
.panel-divider{position:absolute;left:216px;top:19px;width:1px;height:32px;background:#ddd}
.add-btn{position:absolute;left:239px;top:19px;width:81px;height:33px;border:1px solid var(--teal-line);background:var(--teal-soft);font-size:14px;display:flex;align-items:center;justify-content:center;gap:8px;border-radius:2px}
.add-btn svg{width:13px;height:13px;stroke:var(--teal);stroke-width:2}
.view-toggle{position:absolute;left:847px;top:19px;width:60px;height:32px;border:1px solid var(--teal-line);border-radius:4px;display:flex;align-items:center;justify-content:space-around}
.view-toggle .on{background:var(--teal);border-radius:3px;padding:3px}
.icon-btn{position:absolute;left:916px;top:19px;width:31px;height:32px;border:1px solid var(--teal-line);border-radius:4px;display:flex;align-items:center;justify-content:center}
.hline{position:absolute;left:0;right:0;height:1px;background:var(--line)}
.col-head{position:absolute;top:88px;font-size:14px;font-weight:600;display:flex;align-items:center;gap:10px}
.row{position:absolute;left:0;right:0;height:65px;border-bottom:1px solid #f0f0f4}
.row:last-child{border-bottom:0}
.row > *{position:absolute}
.person{left:35px;top:14px;width:38px;height:38px;border-radius:50%}
.who{left:92px;top:14px;font-size:14px;line-height:18px}
.who b{font-weight:400;color:var(--teal);display:block}
.badge{left:235px;top:22px;height:22px;padding:0 10px;border-radius:3px;font-size:9.5px;font-weight:700;color:#fff;display:flex;align-items:center;letter-spacing:.3px}
.badge.assigned{background:var(--green)}.badge.available{background:var(--purple)}
.cell{top:23px;font-size:14px}
.act{top:16px;width:47px;height:33px;border:1px solid var(--teal-line);background:var(--teal-soft);border-radius:3px;display:flex;align-items:center;justify-content:center}
.act.del{background:#fff}
.act svg{width:16px;height:16px;fill:none;stroke:var(--teal);stroke-width:1.7}
.act.del svg{stroke:var(--red)}
</style>
</head>
<body>
<div class="stage">

<!-- ===== Screen variant A ===== -->
<section class="screen first">
  <aside class="sidebar">
    <div class="brand"><span class="brand-dot"></span>ShiftCover</div>
    <div class="nav-item active" style="top:118px"><svg viewBox="0 0 20 20"><path d="M3 9l7-6 7 6v8H3z"/><path d="M8 17v-5h4v5"/></svg>Dashboard</div>
    <div class="nav-item" style="top:159px"><svg viewBox="0 0 20 20"><rect x="3" y="4" width="14" height="13" rx="1"/><path d="M3 8h14M7 2v4M13 2v4"/></svg>Calendar</div>
    <div class="nav-item" style="top:201px"><svg viewBox="0 0 20 20"><circle cx="10" cy="10" r="7"/><path d="M8.5 7l4 3-4 3z"/></svg>Demo Outbox</div>
    <div class="nav-item" style="top:242px"><svg viewBox="0 0 20 20"><circle cx="10" cy="7" r="3.5"/><path d="M3 17c1-4 13-4 14 0z"/></svg>Location Admin<svg class="caret" viewBox="0 0 20 20" style="width:12px"><path d="M7 4l6 6-6 6"/></svg></div>
    <div class="nav-item" style="top:283px"><svg viewBox="0 0 20 20"><circle cx="8" cy="7" r="3"/><path d="M2 17c1-4 11-4 12 0M13 4a3 3 0 010 6M15 12c2 1 3 3 3 5"/></svg>Regular Staff<svg class="caret" viewBox="0 0 20 20" style="width:12px"><path d="M4 7l6 6 6-6"/></svg></div>
    <div class="nav-item sub" style="top:325px"><svg viewBox="0 0 20 20"><circle cx="8" cy="7" r="3"/><path d="M2 17c1-4 10-4 11 0M13 9l2 2 4-4"/></svg>Manage Regular Staff</div>
    <div class="nav-item sub" style="top:366px"><svg viewBox="0 0 20 20"><path d="M10 4H4v13h13v-6"/><path d="M15 2l3 3-8 8H7v-3z"/></svg>Leave Requests</div>
    <div class="nav-item" style="top:408px"><svg viewBox="0 0 20 20"><path d="M8 3H3v14h5M12 6l4 4-4 4M16 10H7"/></svg>Logout</div>
  </aside>

  <div class="avatar-main" role="img" aria-label="Profile photo of the signed-in administrator"></div>
  <div class="welcome">Welcomeback,</div>
  <div class="user-name">Owen Parker<svg viewBox="0 0 14 14"><path d="M2 5l5 5 5-5"/></svg></div>
  <div class="top-btn" style="left:781px;width:128px">Create Vacancy</div>
  <div class="top-btn soft" style="left:916px;width:130px">Create Absence</div>
  <div class="top-btn" style="left:1052px;width:95px">Approve 3</div>
  <div class="top-btn soft" style="left:1154px;width:95px">Approve 8</div>

  <div class="card" style="left:277px">
    <div class="card-title">Total Todays Summary</div>
    <div class="big-num">100</div>
    <div class="meter"><i></i></div>
    <div class="legend l1" style="left:31px"><b>5</b><span>Unfilled</span></div>
    <div class="legend l2" style="left:118px"><b>75</b><span>Filled</span></div>
    <div class="legend l3" style="left:191px"><b>20</b><span>No sub needed</span></div>
  </div>
  <div class="card" style="left:610px">
    <div class="card-title">Total Job Monthly Summary</div>
    <div class="big-num">45</div>
    <div class="meter" style="left:94px;width:190px"><i style="width:10%"></i></div>
    <div class="legend l1" style="left:31px"><b>4</b><span>Unfilled</span></div>
    <div class="legend l2" style="left:104px"><b>12</b><span>Filled Jobs</span></div>
    <div class="legend l3" style="left:191px"><b>29</b><span>No sub needed</span></div>
  </div>
  <div class="card" style="left:944px">
    <div class="card-title">Monthly Filled Rate</div>
    <div class="big-num">123</div>
    <div class="meter" style="left:112px;width:172px"><i style="width:15%"></i></div>
    <div class="legend l1" style="left:31px"><b>27%</b><span>No sub</span></div>
    <div class="legend l2" style="left:134px"><b>33%</b><span>Open</span></div>
    <div class="legend l3" style="left:238px"><b>40%</b><span>Filled</span></div>
  </div>

  <nav class="tabs"><span class="on">Managed Openings</span><span>Regular Staff Leave Req.</span><span>My Leave Req.</span><span>Location Overview</span><span>Pending Profile Images</span><span>Substitute Attendance</span></nav>

  <div class="panel">
    <div class="panel-title">Manage Openings</div>
    <div class="panel-divider"></div>
    <div class="add-btn"><svg viewBox="0 0 14 14"><path d="M7 1v12M1 7h12"/></svg>Add</div>
    <div class="view-toggle"><svg width="16" height="16" viewBox="0 0 20 20" fill="none" stroke="#29b0d3" stroke-width="1.8"><path d="M10 2a8 8 0 108 8h-8z"/></svg><span class="on"><svg width="16" height="16" viewBox="0 0 20 20" stroke="#fff" stroke-width="2"><path d="M3 5h14M3 9h14M3 13h14M3 17h14"/></svg></span></div>
    <div class="icon-btn"><svg width="16" height="16" viewBox="0 0 20 20" fill="none" stroke="#29b0d3" stroke-width="1.8"><path d="M2 3h16l-6 7v6l-4 2v-8z"/></svg></div>
    <div class="hline" style="top:75px"></div>
    <div class="col-head" style="left:35px">Regular Staff</div>
    <div class="col-head" style="left:235px">Status</div>
    <div class="col-head" style="left:350px">Summary<svg width="11" height="11" viewBox="0 0 12 12" fill="none" stroke="#29b0d3" stroke-width="2"><path d="M2 4l4 4 4-4"/></svg></div>
    <div class="col-head" style="left:533px">Location</div>
    <div class="col-head" style="left:628px">Time Slots summary</div>
    <div class="hline" style="top:122px"></div>
    <div style="position:absolute;left:0;right:0;top:125px">
      <div class="row" style="top:0"><div class="person" role="img" aria-label="Staff photo" style="background:#e4ddd6"></div><div class="who"><b>Lena Ortiz</b>Teacher</div><div class="badge assigned">ASSIGNED</div><div class="cell" style="left:350px">Immediate need! Library</div><div class="cell" style="left:536px">WDMS</div><div class="cell" style="left:628px">12/30 - 01/01 (2h 30m)</div><div class="act" style="left:791px"><svg viewBox="0 0 20 20"><path d="M13 3l4 4-9 9H4v-4zM3 18h14"/></svg></div><div class="act" style="left:845px"><svg viewBox="0 0 20 20"><path d="M1 10s3-6 9-6 9 6 9 6-3 6-9 6-9-6-9-6z"/><circle cx="10" cy="10" r="2.5"/></svg></div><div class="act del" style="left:900px"><svg viewBox="0 0 20 20"><path d="M3 5h14M8 5V3h4v2M5 5l1 12h8l1-12M8 8v6M12 8v6"/></svg></div></div>
      <div class="row" style="top:65px"><div class="person" role="img" aria-label="Staff photo" style="background:#cfc9c4"></div><div class="who"><b>Ravi Dunn</b>Food Service</div><div class="badge available">AVAILABLE</div><div class="cell" style="left:350px">Seeking Sub for Couns</div><div class="cell" style="left:536px">WDMS</div><div class="cell" style="left:628px">12/30 - 01/01 (2h 30m)</div><div class="act" style="left:791px"><svg viewBox="0 0 20 20"><path d="M13 3l4 4-9 9H4v-4zM3 18h14"/></svg></div><div class="act" style="left:845px"><svg viewBox="0 0 20 20"><path d="M1 10s3-6 9-6 9 6 9 6-3 6-9 6-9-6-9-6z"/><circle cx="10" cy="10" r="2.5"/></svg></div><div class="act del" style="left:900px"><svg viewBox="0 0 20 20"><path d="M3 5h14M8 5V3h4v2M5 5l1 12h8l1-12M8 8v6M12 8v6"/></svg></div></div>
      <div class="row" style="top:130px"><div class="person" role="img" aria-label="Staff photo" style="background:#4f6f80"></div><div class="who"><b>Clara Mendes</b>Food Service</div><div class="badge available">AVAILABLE</div><div class="cell" style="left:350px">Seeking Sub for IT</div><div class="cell" style="left:536px">FMS</div><div class="cell" style="left:628px">12/30 - 01/01 (2h 30m)</div><div class="act" style="left:791px"><svg viewBox="0 0 20 20"><path d="M13 3l4 4-9 9H4v-4zM3 18h14"/></svg></div><div class="act" style="left:845px"><svg viewBox="0 0 20 20"><path d="M1 10s3-6 9-6 9 6 9 6-3 6-9 6-9-6-9-6z"/><circle cx="10" cy="10" r="2.5"/></svg></div><div class="act del" style="left:900px"><svg viewBox="0 0 20 20"><path d="M3 5h14M8 5V3h4v2M5 5l1 12h8l1-12M8 8v6M12 8v6"/></svg></div></div>
      <div class="row" style="top:195px"><div class="person" role="img" aria-label="Staff photo" style="background:#e8b43c"></div><div class="who"><b>Ivy Holt</b>Teacher’s Aide</div><div class="badge available">AVAILABLE</div><div class="cell" style="left:350px">Substitute &nbsp;needed for ..</div><div class="cell" style="left:536px">FMS</div><div class="cell" style="left:628px">12/30 - 01/01 (2h 30m)</div><div class="act" style="left:791px"><svg viewBox="0 0 20 20"><path d="M13 3l4 4-9 9H4v-4zM3 18h14"/></svg></div><div class="act" style="left:845px"><svg viewBox="0 0 20 20"><path d="M1 10s3-6 9-6 9 6 9 6-3 6-9 6-9-6-9-6z"/><circle cx="10" cy="10" r="2.5"/></svg></div><div class="act del" style="left:900px"><svg viewBox="0 0 20 20"><path d="M3 5h14M8 5V3h4v2M5 5l1 12h8l1-12M8 8v6M12 8v6"/></svg></div></div>
      <div class="row" style="top:260px"><div class="person" role="img" aria-label="Staff photo" style="background:#d9d2cc"></div><div class="who"><b>Tessa Obi</b>Teacher</div><div class="badge available">AVAILABLE</div><div class="cell" style="left:350px">Seeking Sub for Couns</div><div class="cell" style="left:536px">FMS</div><div class="cell" style="left:628px">12/30 - 01/01 (2h 30m)</div><div class="act" style="left:791px"><svg viewBox="0 0 20 20"><path d="M13 3l4 4-9 9H4v-4zM3 18h14"/></svg></div><div class="act" style="left:845px"><svg viewBox="0 0 20 20"><path d="M1 10s3-6 9-6 9 6 9 6-3 6-9 6-9-6-9-6z"/><circle cx="10" cy="10" r="2.5"/></svg></div><div class="act del" style="left:900px"><svg viewBox="0 0 20 20"><path d="M3 5h14M8 5V3h4v2M5 5l1 12h8l1-12M8 8v6M12 8v6"/></svg></div></div>
    </div>
  </div>
</section>

<!-- ===== Screen variant B ===== -->
<section class="screen second">
  <aside class="sidebar">
    <div class="brand"><span class="brand-dot"></span>ShiftCover</div>
    <div class="nav-item active" style="top:118px"><svg viewBox="0 0 20 20"><path d="M3 9l7-6 7 6v8H3z"/><path d="M8 17v-5h4v5"/></svg>Dashboard</div>
    <div class="nav-item" style="top:159px"><svg viewBox="0 0 20 20"><rect x="3" y="4" width="14" height="13" rx="1"/><path d="M3 8h14M7 2v4M13 2v4"/></svg>Calendar</div>
    <div class="nav-item" style="top:201px"><svg viewBox="0 0 20 20"><circle cx="10" cy="10" r="7"/><path d="M8.5 7l4 3-4 3z"/></svg>Demo Outbox</div>
    <div class="nav-item" style="top:242px"><svg viewBox="0 0 20 20"><circle cx="10" cy="7" r="3.5"/><path d="M3 17c1-4 13-4 14 0z"/></svg>Location Admin<svg class="caret" viewBox="0 0 20 20" style="width:12px"><path d="M7 4l6 6-6 6"/></svg></div>
    <div class="nav-item" style="top:283px"><svg viewBox="0 0 20 20"><circle cx="8" cy="7" r="3"/><path d="M2 17c1-4 11-4 12 0M13 4a3 3 0 010 6M15 12c2 1 3 3 3 5"/></svg>Regular Staff<svg class="caret" viewBox="0 0 20 20" style="width:12px"><path d="M4 7l6 6 6-6"/></svg></div>
    <div class="nav-item sub" style="top:325px"><svg viewBox="0 0 20 20"><circle cx="8" cy="7" r="3"/><path d="M2 17c1-4 10-4 11 0M13 9l2 2 4-4"/></svg>Manage Regular Staff</div>
    <div class="nav-item sub" style="top:366px"><svg viewBox="0 0 20 20"><path d="M10 4H4v13h13v-6"/><path d="M15 2l3 3-8 8H7v-3z"/></svg>Leave Requests</div>
    <div class="nav-item" style="top:408px"><svg viewBox="0 0 20 20"><path d="M8 3H3v14h5M12 6l4 4-4 4M16 10H7"/></svg>Logout</div>
  </aside>

  <div class="avatar-main" role="img" aria-label="Profile photo of the signed-in administrator"></div>
  <div class="welcome">Welcomeback,</div>
  <div class="user-name">Owen Parker<svg viewBox="0 0 14 14"><path d="M2 5l5 5 5-5"/></svg></div>
  <div class="top-btn" style="left:781px;width:128px">Create Vacancy</div>
  <div class="top-btn soft" style="left:916px;width:130px">Create Absence</div>
  <div class="top-btn" style="left:1052px;width:95px">Approve 3</div>
  <div class="top-btn soft" style="left:1154px;width:95px">Approve 8</div>

  <div class="card" style="left:277px">
    <div class="card-title">Total Todays Summary</div>
    <div class="big-num">100</div>
    <div class="meter thick"><i></i></div>
    <div class="legend l1" style="left:31px"><b>5</b><span>Unfilled</span></div>
    <div class="legend l2" style="left:118px"><b>75</b><span>Filled</span></div>
    <div class="legend l3" style="left:191px"><b>20</b><span>No sub needed</span></div>
  </div>
  <div class="card" style="left:610px">
    <div class="card-title">Total Job Monthly Summary</div>
    <div class="cbar" style="left:33px;top:76px;width:52px;height:28px;background:var(--purple);color:#fff">30</div>
    <div class="cbar" style="left:97px;top:64px;width:52px;height:9px;background:var(--purple-mid)"></div>
    <div class="cbar" style="left:97px;top:78px;width:52px;height:24px">10</div>
    <div class="cbar" style="left:161px;top:56px;width:52px;height:7px;background:var(--purple-light)"></div>
    <div class="cbar" style="left:161px;top:78px;width:52px;height:24px">5</div>
    <div class="cbar" style="left:225px;top:55px;width:52px;height:49px;background:var(--teal);color:#fff;font-size:34px">45</div>
    <div class="cbar-label" style="left:33px">Unfilled</div>
    <div class="cbar-label" style="left:97px">Filled Job</div>
    <div class="cbar-label" style="left:161px">No sub</div>
    <div class="cbar-label" style="left:225px">Total</div>
  </div>
  <div class="card" style="left:944px">
    <div class="card-title">Monthly Filled Rate</div>
    <div class="axis" style="left:6px;top:48px">100%</div>
    <div class="axis" style="left:6px;top:81px">50%</div>
    <div class="axis" style="left:6px;top:114px">0</div>
    <div class="stack" style="top:54px;height:17px;background:var(--purple-light)">27%</div>
    <div class="stack" style="top:71px;height:21px;background:var(--purple-mid)">33%</div>
    <div class="stack" style="top:92px;height:30px;background:var(--purple)">40%</div>
    <div class="hline" style="left:56px;right:124px;top:121px;background:#ddd"></div>
    <div class="side-legend l1" style="top:54px">No sub</div>
    <div class="side-legend l2" style="top:76px">Open</div>
    <div class="side-legend l3" style="top:98px">Filled</div>
  </div>

  <nav class="tabs"><span class="on">Managed Openings</span><span>Regular Staff Leave Req.</span><span>My Leave Req.</span><span>Location Overview</span><span>Pending Profile Images</span><span>Substitute Attendance</span></nav>

  <div class="panel">
    <div class="panel-title">Manage Openings</div>
    <div class="panel-divider"></div>
    <div class="add-btn"><svg viewBox="0 0 14 14"><path d="M7 1v12M1 7h12"/></svg>Add</div>
    <div class="view-toggle"><svg width="16" height="16" viewBox="0 0 20 20" fill="none" stroke="#29b0d3" stroke-width="1.8"><path d="M10 2a8 8 0 108 8h-8z"/></svg><span class="on"><svg width="16" height="16" viewBox="0 0 20 20" stroke="#fff" stroke-width="2"><path d="M3 5h14M3 9h14M3 13h14M3 17h14"/></svg></span></div>
    <div class="icon-btn"><svg width="16" height="16" viewBox="0 0 20 20" fill="none" stroke="#29b0d3" stroke-width="1.8"><path d="M2 3h16l-6 7v6l-4 2v-8z"/></svg></div>
    <div class="hline" style="top:75px"></div>
    <div class="col-head" style="left:35px">Regular Staff</div>
    <div class="col-head" style="left:235px">Status</div>
    <div class="col-head" style="left:350px">Summary<svg width="11" height="11" viewBox="0 0 12 12" fill="none" stroke="#29b0d3" stroke-width="2"><path d="M2 4l4 4 4-4"/></svg></div>
    <div class="col-head" style="left:533px">Location</div>
    <div class="col-head" style="left:628px">Time Slots summary</div>
    <div class="hline" style="top:122px"></div>
    <div style="position:absolute;left:0;right:0;top:125px">
      <div class="row" style="top:0"><div class="person" role="img" aria-label="Staff photo" style="background:#e4ddd6"></div><div class="who"><b>Lena Ortiz</b>Teacher</div><div class="badge assigned">ASSIGNED</div><div class="cell" style="left:350px">Immediate need! Library</div><div class="cell" style="left:536px">WDMS</div><div class="cell" style="left:628px">12/30 - 01/01 (2h 30m)</div><div class="act" style="left:791px"><svg viewBox="0 0 20 20"><path d="M13 3l4 4-9 9H4v-4zM3 18h14"/></svg></div><div class="act" style="left:845px"><svg viewBox="0 0 20 20"><path d="M1 10s3-6 9-6 9 6 9 6-3 6-9 6-9-6-9-6z"/><circle cx="10" cy="10" r="2.5"/></svg></div><div class="act del" style="left:900px"><svg viewBox="0 0 20 20"><path d="M3 5h14M8 5V3h4v2M5 5l1 12h8l1-12M8 8v6M12 8v6"/></svg></div></div>
      <div class="row" style="top:65px"><div class="person" role="img" aria-label="Staff photo" style="background:#cfc9c4"></div><div class="who"><b>Ravi Dunn</b>Food Service</div><div class="badge available">AVAILABLE</div><div class="cell" style="left:350px">Seeking Sub for Couns</div><div class="cell" style="left:536px">WDMS</div><div class="cell" style="left:628px">12/30 - 01/01 (2h 30m)</div><div class="act" style="left:791px"><svg viewBox="0 0 20 20"><path d="M13 3l4 4-9 9H4v-4zM3 18h14"/></svg></div><div class="act" style="left:845px"><svg viewBox="0 0 20 20"><path d="M1 10s3-6 9-6 9 6 9 6-3 6-9 6-9-6-9-6z"/><circle cx="10" cy="10" r="2.5"/></svg></div><div class="act del" style="left:900px"><svg viewBox="0 0 20 20"><path d="M3 5h14M8 5V3h4v2M5 5l1 12h8l1-12M8 8v6M12 8v6"/></svg></div></div>
      <div class="row" style="top:130px"><div class="person" role="img" aria-label="Staff photo" style="background:#4f6f80"></div><div class="who"><b>Clara Mendes</b>Food Service</div><div class="badge available">AVAILABLE</div><div class="cell" style="left:350px">Seeking Sub for IT</div><div class="cell" style="left:536px">FMS</div><div class="cell" style="left:628px">12/30 - 01/01 (2h 30m)</div><div class="act" style="left:791px"><svg viewBox="0 0 20 20"><path d="M13 3l4 4-9 9H4v-4zM3 18h14"/></svg></div><div class="act" style="left:845px"><svg viewBox="0 0 20 20"><path d="M1 10s3-6 9-6 9 6 9 6-3 6-9 6-9-6-9-6z"/><circle cx="10" cy="10" r="2.5"/></svg></div><div class="act del" style="left:900px"><svg viewBox="0 0 20 20"><path d="M3 5h14M8 5V3h4v2M5 5l1 12h8l1-12M8 8v6M12 8v6"/></svg></div></div>
      <div class="row" style="top:195px"><div class="person" role="img" aria-label="Staff photo" style="background:#e8b43c"></div><div class="who"><b>Ivy Holt</b>Teacher’s Aide</div><div class="badge available">AVAILABLE</div><div class="cell" style="left:350px">Substitute &nbsp;needed for ..</div><div class="cell" style="left:536px">FMS</div><div class="cell" style="left:628px">12/30 - 01/01 (2h 30m)</div><div class="act" style="left:791px"><svg viewBox="0 0 20 20"><path d="M13 3l4 4-9 9H4v-4zM3 18h14"/></svg></div><div class="act" style="left:845px"><svg viewBox="0 0 20 20"><path d="M1 10s3-6 9-6 9 6 9 6-3 6-9 6-9-6-9-6z"/><circle cx="10" cy="10" r="2.5"/></svg></div><div class="act del" style="left:900px"><svg viewBox="0 0 20 20"><path d="M3 5h14M8 5V3h4v2M5 5l1 12h8l1-12M8 8v6M12 8v6"/></svg></div></div>
      <div class="row" style="top:260px"><div class="person" role="img" aria-label="Staff photo" style="background:#d9d2cc"></div><div class="who"><b>Tessa Obi</b>Teacher</div><div class="badge available">AVAILABLE</div><div class="cell" style="left:350px">Seeking Sub for Couns</div><div class="cell" style="left:536px">FMS</div><div class="cell" style="left:628px">12/30 - 01/01 (2h 30m)</div><div class="act" style="left:791px"><svg viewBox="0 0 20 20"><path d="M13 3l4 4-9 9H4v-4zM3 18h14"/></svg></div><div class="act" style="left:845px"><svg viewBox="0 0 20 20"><path d="M1 10s3-6 9-6 9 6 9 6-3 6-9 6-9-6-9-6z"/><circle cx="10" cy="10" r="2.5"/></svg></div><div class="act del" style="left:900px"><svg viewBox="0 0 20 20"><path d="M3 5h14M8 5V3h4v2M5 5l1 12h8l1-12M8 8v6M12 8v6"/></svg></div></div>
    </div>
  </div>
</section>

</div>
</body>
</html>
```